Quill Contracting - general earthmoving business in Central Queensland

Quill Contracting is an existing company but now branching into other areas of earthmoving. We are based in Central Queensland.
We would like to use the advertisement in our local newspaper, but other areas as required.
We have attached our existing advertisement as we would like something similar, but also including our new machine and details
Industry/Entity Type
Business
Requirements
Must have
- Please include the following points:
- All general earthmoving- Dozer & Loader
- New Dams & Turkey's Nests
- Dam de-silting and repairs
- Cutter-barring
- Timber Thinning- to meet all new government regulations
- Scrub Pulling
Please also include the photos attached, OR digital images of a Loader and Dozer (as per header attached)

```html
<!DOCTYPE html>
<html lang="en">
<head>
<meta charset="utf-8">
<title>Quill Contracting – Newspaper Advertisement</title>
<link rel="stylesheet" href="https://fonts.googleapis.com/css2?family=Arimo:wght@700&display=swap">
<style>
  :root {
    --black: #000000;
    --white: #ffffff;
    --orange: #f15a22;
    --cream: #fdfad5;
    --machine-yellow: #d9b42a;
    --machine-dark: #8a6d12;
    --frame: #555555;
  }
  * { box-sizing: border-box; margin: 0; padding: 0; }
  html, body { width: 1200px; height: 1000px; overflow: hidden; background: var(--white); }
  body { position: relative; font-family: "Arimo", Arial, sans-serif; font-weight: 700; }

  .ad { position: absolute; left: 205px; width: 789px; border: 2px solid var(--frame); }
  .ad--dark-left { top: 22px; height: 477px; background: var(--black); }
  .ad--light-left { top: 503px; height: 473px; background: var(--black); border-color: var(--frame); }

  .machines { position: absolute; left: 0; top: 0; width: 393px; height: 100%; }
  .ad--dark-left .machines { background: var(--black); }
  .ad--light-left .machines { background: var(--cream); }

  .machine-art {
    position: absolute;
    border-radius: 10px;
    background: radial-gradient(ellipse at 45% 45%, var(--machine-yellow) 0%, #c49a1c 55%, var(--machine-dark) 100%);
  }

  .info { position: absolute; left: 393px; top: 0; right: 0; height: 100%; }
  .ad--dark-left .info { background: var(--white); border: 4px solid var(--black); }
  .ad--light-left .info { background: var(--black); }

  .brand-name {
    position: absolute; left: 0; right: 0; text-align: center;
    color: var(--orange); line-height: 1; letter-spacing: 1px;
  }
  .brand-name .brand-main { display: block; font-size: 76px; }
  .brand-name .brand-sub { display: block; font-size: 46px; margin-top: 8px; }

  .torn-band { position: absolute; left: 12px; top: 178px; width: 364px; height: 246px; }

  .services-tag {
    position: absolute; background: var(--orange); color: var(--white);
    font-size: 23px; line-height: 28px; padding: 0 8px; border-radius: 0 4px 4px 0;
  }

  .service-list { position: absolute; list-style: none; color: var(--white); font-size: 17.5px; line-height: 20.8px; }
  .service-list li { position: relative; padding-left: 13px; }
  .service-list li::before {
    content: ""; position: absolute; left: 0; top: 8px; width: 4px; height: 4px; background: var(--orange); border-radius: 50%;
  }

  .service-lines { position: absolute; left: 0; right: 0; text-align: center; color: var(--white); font-size: 17.5px; line-height: 19.7px; }

  .contact {
    position: absolute; background: var(--orange); font-size: 21px; line-height: 30px;
    text-align: center; border-radius: 0 5px 5px 0;
  }
  .ad--dark-left .contact { color: var(--black); }
  .ad--light-left .contact { color: var(--white); }
</style>
</head>
<body>

  <section class="ad ad--dark-left">
    <div class="machines">
      <div class="machine-art" style="left:40px; top:38px; width:305px; height:218px;" role="img" aria-label="Illustration of a yellow crawler dozer with front blade"></div>
      <div class="machine-art" style="left:35px; top:274px; width:322px; height:182px;" role="img" aria-label="Illustration of a yellow wheel loader with front bucket"></div>
    </div>
    <div class="info">
      <h1 class="brand-name" style="top:28px;">
        <span class="brand-main">QUILL</span>
        <span class="brand-sub">CONTRACTING</span>
      </h1>
      <svg class="torn-band" viewBox="0 0 364 246" aria-hidden="true">
        <polygon fill="#000" points="0,8 10,2 18,10 30,4 42,12 55,3 66,9 80,1 92,10 105,4 118,11 132,2 144,9 158,3 170,12 184,4 198,10 212,2 226,11 240,3 252,9 266,1 280,10 294,4 306,12 320,3 334,9 348,2 364,8 364,232 352,240 340,234 326,244 312,236 298,242 284,233 270,243 256,235 242,241 228,232 214,244 200,236 186,242 172,233 158,244 144,235 130,241 116,232 102,243 88,236 74,242 60,233 46,244 32,235 18,241 8,234 0,240"/>
      </svg>
      <div class="services-tag" style="left:45px; top:195px;">SERVICES</div>
      <ul class="service-list" style="left:46px; top:232px;">
        <li>All general earthmoving<br>Dozer &amp; Loader,</li>
        <li>New Dams &amp; Turkey's Nests,</li>
        <li>Dam de-silting and repairs,</li>
        <li>Cutter-barring,</li>
        <li>Timber Thinning- to meet all new<br>government regulations,</li>
        <li>Scrub Pulling</li>
      </ul>
      <p class="contact" style="left:55px; top:431px; width:282px;">Contact: 0400 612 835</p>
    </div>
  </section>

  <section class="ad ad--light-left">
    <div class="machines">
      <div class="machine-art" style="left:42px; top:30px; width:312px; height:228px;" role="img" aria-label="Illustration of a yellow crawler dozer with front blade"></div>
      <div class="machine-art" style="left:42px; top:270px; width:330px; height:182px;" role="img" aria-label="Illustration of a yellow wheel loader with front bucket"></div>
    </div>
    <div class="info">
      <h1 class="brand-name" style="top:44px;">
        <span class="brand-main">QUILL</span>
        <span class="brand-sub">CONTRACTING</span>
      </h1>
      <div class="services-tag" style="left:125px; top:197px;">SERVICES</div>
      <p class="service-lines" style="top:238px;">
        All general earthmoving- Dozer &amp; Loader,<br>
        New Dams &amp; Turkey's Nests,<br>
        Dam de-silting and repairs,<br>
        Cutter-barring,<br>
        Timber Thinning- to meet all new<br>
        government regulations,<br>
        Scrub Pulling
      </p>
      <p class="contact" style="left:63px; top:402px; width:266px;">Contact: 0400 612 835</p>
    </div>
  </section>

</body>
</html>
```